TriVex Business Card Design - double sided -plumbing local plumbing company

We have a Plumbing company where the design was create through Sketch Hive. We would now like a business card designed as well. We want it to be in the colour version of the logo.

Details below for the card.

Phone Number: 0438 615 247
Email: info@trivexplumbing.example.au
Website: https://trivexplumbing.example.au
We really want a sophisticated design that stand out from the other- informative and timeless.

Target Market(s)

local Canberra market

Industry/Entity Type

Plumbing, gas fitting, hot water

Contact Information for Business Card

Phone number, email, logo and "Supplying all your heating, cooling and hot water needs"

Requirements
Must have
• bust be colourful, must also be though about it being printed on a magnet. must Vex with the logo - I dont want the logo and information chucked onto a white canvas I would prefer it to be smooth and look purposeful

```html
<!DOCTYPE html>
<html lang="en">
<head>
<meta charset="utf-8">
<title>TriVex Plumbing – Business Card</title>
<link rel="stylesheet" href="https://fonts.googleapis.com/css2?family=Montserrat:ital,wght@0,400;0,700;0,800;1,400&display=swap">
<style>
  :root {
    --stage: #1d1d1f;
    --sky: #03aeef;
    --sky-light: #3cc2f4;
    --sun: #f9a93a;
    --ink: #3a3a3a;
    --paper: #ffffff;
  }
  * { box-sizing: border-box; margin: 0; padding: 0; }
  html, body {
    width: 1200px; height: 900px; overflow: hidden;
    background: var(--stage);
    font-family: "Montserrat", Arial, sans-serif;
  }
  .stage {
    width: 1200px; height: 900px;
    display: flex; flex-direction: column;
    align-items: center; justify-content: center; gap: 50px;
  }
  .card {
    position: relative;
    width: 630px; height: 360px;
    border-radius: 4px;
    overflow: hidden;
    box-shadow: 0 14px 30px rgba(0,0,0,.5);
  }

  /* Front */
  .card--front { background: var(--paper); color: var(--ink); }
  .brand {
    position: absolute;
    font-weight: 800;
    letter-spacing: 2px;
    display: flex; align-items: center; gap: 12px;
  }
  .card--front .brand {
    top: 62px; left: 236px;
    font-size: 64px; color: var(--sky);
  }
  .brand__dot {
    width: 28px; height: 28px; border-radius: 50%;
    background: var(--sun);
  }
  .holder { position: absolute; left: 40px; top: 186px; width: 250px; text-align: right; }
  .holder__name { font-weight: 800; font-size: 24px; letter-spacing: 1px; line-height: 1.1; }
  .holder__first { color: var(--sky); }
  .holder__last { color: var(--sun); }
  .holder__role { font-size: 15px; margin-top: 4px; color: var(--ink); }
  .divider {
    position: absolute; left: 310px; top: 182px;
    width: 1.5px; height: 82px; background: var(--sun);
  }
  .contact { position: absolute; left: 332px; top: 186px; list-style: none; }
  .contact li {
    display: flex; align-items: center; gap: 9px;
    font-size: 14px; line-height: 26px;
  }
  .contact svg { width: 13px; height: 13px; fill: var(--sky); flex: none; }
  .address {
    position: absolute; left: 0; right: 0; bottom: 32px;
    text-align: center; font-size: 14.5px; color: var(--ink);
  }

  /* Back */
  .card--back {
    background:
      radial-gradient(ellipse 60% 90% at 20% 20%, var(--sky-light), transparent 70%),
      radial-gradient(ellipse 50% 80% at 85% 90%, var(--sky-light), transparent 70%),
      var(--sky);
  }
  .card--back .brand {
    top: 108px; left: 0; right: 0; justify-content: center;
    font-size: 76px; color: var(--paper);
  }
  .card--back .brand__dot { background: var(--paper); width: 32px; height: 32px; }
  .tagline {
    position: absolute; left: 0; right: 0; top: 226px;
    text-align: center; color: var(--paper); font-size: 17px;
  }
</style>
</head>
<body>
<main class="stage">

  <section class="card card--front" aria-label="Business card front">
    <div class="brand">TRIVEX<span class="brand__dot"></span></div>

    <div class="holder">
      <p class="holder__name"><span class="holder__first">LIAM</span> <span class="holder__last">HARCOURT</span></p>
      <p class="holder__role">Owner &amp; Manager</p>
    </div>

    <div class="divider"></div>

    <ul class="contact">
      <li>
        <svg viewBox="0 0 24 24" aria-hidden="true"><path d="M6.6 10.8a15.1 15.1 0 0 0 6.6 6.6l2.2-2.2a1 1 0 0 1 1-.25 11.4 11.4 0 0 0 3.6.57 1 1 0 0 1 1 1V20a1 1 0 0 1-1 1A17 17 0 0 1 3 4a1 1 0 0 1 1-1h3.5a1 1 0 0 1 1 1c0 1.25.2 2.45.57 3.57a1 1 0 0 1-.25 1z"/></svg>
        0438 615 247
      </li>
      <li>
        <svg viewBox="0 0 24 24" aria-hidden="true"><path d="M2 5h20v14H2z M2 5l10 8 10-8" stroke="#fff" stroke-width="1.5"/></svg>
        info@trivexplumbing.example.au
      </li>
      <li>
        <svg viewBox="0 0 24 24" aria-hidden="true"><circle cx="12" cy="12" r="10"/></svg>
        www.trivexplumbing.example.au
      </li>
    </ul>

    <p class="address">P.O. Box Wren Street Country Name AB, H7B 2K9</p>
  </section>

  <section class="card card--back" aria-label="Business card back">
    <div class="brand">TRIVEX<span class="brand__dot"></span></div>
    <p class="tagline">Supplying all your heating, cooling and hot water needs</p>
  </section>

</main>
</body>
</html>
```